Business Cards Letter Head Financial Trading Company
Bus Cards Letter Head Compliment Slips
Simple
Oliver Petchley
Managing Director
Level 52
8 Harrow Crescent
Fenmoor Quay
London
E17 3RT
oliver.petchley@zqtrading.co.uk
www.zoltavequitytrading.co.uk
Would like additional cards for other employees
Logo on back page

```html
<!DOCTYPE html>
<html lang="en">
<head>
<meta charset="utf-8">
<title>Zoltav Equity Trading — Stationery Concepts</title>
<link href="https://fonts.googleapis.com/css2?family=Montserrat:wght@400;600;700&display=swap" rel="stylesheet">
<style>
  :root {
    --navy: #2f2b7c;
    --gold: #c9a24b;
    --gold-soft: #e8d7ad;
    --paper: #ffffff;
    --ink: #55556a;
    --stage: #e7e4df;
    --label: #6f6b66;
  }
  * { box-sizing: border-box; margin: 0; padding: 0; }
  html, body { width: 1200px; height: 466px; overflow: hidden; }
  body {
    background: var(--stage);
    font-family: "Montserrat", Arial, sans-serif;
    color: var(--ink);
    position: relative;
  }
  .label {
    position: absolute;
    font-size: 4px;
    letter-spacing: 1px;
    text-transform: uppercase;
    color: var(--label);
    white-space: nowrap;
  }
  .label-section { font-size: 6px; }
  .sheet {
    position: absolute;
    background: var(--paper);
    box-shadow: 0 2px 6px rgba(0,0,0,.18);
  }
  .brand {
    display: flex;
    align-items: center;
    gap: 4px;
    color: var(--navy);
    font-weight: 700;
    white-space: nowrap;
  }
  .brand-dot {
    border-radius: 50%;
    background: var(--gold);
    flex: none;
  }

  /* business cards */
  .card { width: 74px; height: 42px; left: 22px; }
  .card-front { top: 150px; display: flex; align-items: center; justify-content: center; }
  .card-front .brand { font-size: 5px; }
  .card-front .brand-dot { width: 6px; height: 6px; }
  .card-back { top: 224px; padding: 5px 6px; font-size: 2.6px; line-height: 1.35; }
  .card-back .name { color: var(--navy); font-weight: 700; font-size: 3.4px; }
  .card-back .brand { position: absolute; right: 5px; bottom: 5px; font-size: 3px; }
  .card-back .brand-dot { width: 4px; height: 4px; }

  /* letterheads */
  .letterhead { top: 34px; width: 298px; height: 404px; }
  .letterhead-1 { left: 132px; }
  .letterhead-2 { left: 456px; }
  .letterhead .brand { position: absolute; left: 26px; top: 24px; font-size: 8px; }
  .letterhead .brand-dot { width: 9px; height: 9px; }
  .contact-list {
    position: absolute; left: 178px; top: 20px;
    list-style: none; font-size: 3.6px; line-height: 5.4px;
    white-space: nowrap;
  }
  .contact-list li::before {
    content: ""; display: inline-block; width: 3px; height: 3px;
    border-radius: 50%; background: var(--gold); margin-right: 3px; vertical-align: middle;
  }
  .globe-mark {
    position: absolute; left: 70px; top: 150px; width: 150px; height: 150px; border-radius: 50%;
    background: radial-gradient(circle at 40% 40%, #fbf7ee 0%, #f1e8d4 55%, #f7f4fb 80%, rgba(255,255,255,0) 100%);
    opacity: .8;
  }
  .letterhead-2 .globe-mark { left: 60px; top: 140px; width: 170px; height: 170px; }
  .footer-line {
    position: absolute; left: 0; right: 0; bottom: 16px; text-align: center;
    font-size: 3.4px; letter-spacing: .3px; white-space: nowrap;
  }

  /* envelopes */
  .envelopes { position: absolute; left: 790px; top: 34px; }
  .envelope-front {
    position: absolute; left: 790px; top: 300px; width: 400px; height: 128px;
  }
  .envelope-front .brand { position: absolute; left: 16px; top: 14px; font-size: 7px; }
  .envelope-front .brand-dot { width: 8px; height: 8px; }
  .envelope-front .sender { position: absolute; left: 16px; top: 30px; font-size: 3.4px; line-height: 5px; }
</style>
</head>
<body>

  <span class="label label-section" style="left:12px; top:134px;">Stationery Concepts</span>

  <div class="sheet card card-front">
    <div class="brand"><span class="brand-dot"></span>Zoltav Equity Trading</div>
  </div>
  <span class="label" style="left:22px; top:200px;">Business Card Front</span>

  <div class="sheet card card-back">
    <p class="name">Oliver Petchley</p>
    <p>Managing Director</p>
    <p>Level 52, 8 Harrow Crescent</p>
    <p>Fenmoor Quay, London E17 3RT</p>
    <p>oliver.petchley@zqtrading.co.uk</p>
    <div class="brand"><span class="brand-dot"></span>Zoltav Equity Trading</div>
  </div>
  <span class="label" style="left:22px; top:274px;">Business Card Back</span>

  <section class="sheet letterhead letterhead-1">
    <div class="brand"><span class="brand-dot"></span>Zoltav Equity Trading</div>
    <ul class="contact-list">
      <li>Level 52, 8 Harrow Crescent</li>
      <li>Fenmoor Quay, London E17 3RT</li>
      <li>T 020 7946 0381</li>
      <li>oliver.petchley@zqtrading.co.uk</li>
      <li>www.zoltavequitytrading.co.uk</li>
    </ul>
    <div class="globe-mark" role="img" aria-label="Faint brand globe watermark"></div>
  </section>
  <span class="label" style="left:250px; top:450px;">Letter Head Option 1</span>

  <section class="sheet letterhead letterhead-2">
    <div class="brand"><span class="brand-dot"></span>Zoltav Equity Trading</div>
    <div class="globe-mark" role="img" aria-label="Faint brand globe watermark"></div>
    <p class="footer-line">Level 52 · 8 Harrow Crescent · Fenmoor Quay · London E17 3RT · T 020 7946 0381 · www.zoltavequitytrading.co.uk</p>
  </section>
  <span class="label" style="left:574px; top:450px;">Letter Head Option 2</span>

  <svg class="envelopes" width="400" height="256" viewBox="0 0 400 256" aria-hidden="true">
    <rect x="0" y="0" width="400" height="96" fill="var(--navy)"/>
    <polygon points="0,30 200,70 400,30 400,96 0,96" fill="#fff"/>
    <rect x="0" y="96" width="400" height="70" fill="var(--gold)"/>
    <rect x="0" y="96" width="400" height="8" fill="var(--gold-soft)"/>
    <rect x="0" y="150" width="400" height="104" fill="#fff" stroke="#ddd" stroke-width=".6"/>
    <polyline points="0,150 200,205 400,150" fill="none" stroke="#cfcfcf" stroke-width=".8"/>
    <polyline points="0,254 170,198" fill="none" stroke="#e2e2e2" stroke-width=".6"/>
    <polyline points="400,254 230,198" fill="none" stroke="#e2e2e2" stroke-width=".6"/>
    <circle cx="200" cy="205" r="5" fill="var(--gold)"/>
  </svg>
  <span class="label" style="left:950px; top:292px;">Envelope Option 1</span>

  <div class="sheet envelope-front">
    <div class="brand"><span class="brand-dot"></span>Zoltav Equity Trading</div>
    <div class="sender">
      <p>Level 52, 8 Harrow Crescent</p>
      <p>Fenmoor Quay, London E17 3RT</p>
      <p>www.zoltavequitytrading.co.uk</p>
    </div>
  </div>

</body>
</html>
```